Graphically Interesting Large Poster (55x35?)

We are in need of a "Referral Culture Big Board". After design, the board will be printed and therefore rectangular is likely best. About 55x35. There are six sections: 1) Referral Culture Stories 2) Why Growth is Necessary, 3) Origin Story, 4) Client Value Proposition, 5) Singular Concept, 6) Ideal Client (all attached). Not necessarily to be graphically represented in that order. We feel that they are all connected, but not sure how to design the connection. The Referral Culture Stories drive the others. Just an idea. Include our logo prominently. Also attached is the first round of the board (file title: Big Board). Not pretty, not exciting, use that as a DON'T.

Target Market(s)

Internal use for professional financial planning team

Industry/Entity Type

Financial Planning

Font styles to use
Serif

Colors

Designer to choose colors to be used in the design.

Requirements
Must have
• Prominent Logo
• Engaging colors
• Great graphics
• Flow
Nice to have
• Perhaps circular design, with stories in the middle?
• Nice colors, not necessarily matching our logo
Should not have
• Simple text and bullets

```html
<!DOCTYPE html>
<html lang="en">
<head>
<meta charset="utf-8">
<title>Referral Culture Big Board</title>
<link rel="stylesheet" href="https://fonts.googleapis.com/css2?family=Oswald:wght@500&family=Noto+Serif:wght@400&display=swap">
<style>
  :root {
    --sky: #dcedf4;
    --cloud: #ffffff;
    --ink: #3d3d3d;
    --red: #ee5a5e;
    --red-deep: #e3393f;
    --red-soft: #f36f72;
    --red-halo: #f58d90;
    --green: #8dc63f;
    --green-deep: #6e9f2c;
    --green-soft: #a3cd3a;
    --green-halo: #b5d75e;
    --teal: #2fb3c6;
    --teal-deep: #1fa3b1;
    --teal-soft: #4fc1cf;
    --teal-halo: #6ccbd6;
    --orange: #f26a2a;
    --orange-soft: #f5954a;
    --purple: #4a3a8c;
    --purple-deep: #5a4597;
    --purple-soft: #7a63ad;
    --purple-halo: #8d7bb8;
    --yellow: #f7a823;
    --yellow-soft: #fcc636;
    --yellow-halo: #fbd35e;
    --navy: #1d3557;
  }
  * { margin: 0; padding: 0; box-sizing: border-box; }
  html, body { width: 1200px; height: 763px; overflow: hidden; background: var(--sky); }
  .board { position: relative; width: 1200px; height: 763px; background: var(--sky); overflow: hidden; }
  .board__art { position: absolute; inset: 0; }
  .topic { position: absolute; }
  .topic__title {
    font-family: "Oswald", "Arial Narrow", sans-serif;
    font-weight: 500;
    font-size: 19px;
    line-height: 23px;
    text-transform: uppercase;
    white-space: nowrap;
  }
  .topic__body {
    margin-top: 6px;
    font-family: "Noto Serif", Georgia, serif;
    font-size: 9.5px;
    line-height: 11.5px;
    color: var(--ink);
  }
  .topic--growth { left: 395px; top: 60px; width: 150px; text-align: center; }
  .topic--growth .topic__title { color: var(--teal); white-space: normal; }
  .topic--referral { left: 60px; top: 243px; width: 202px; text-align: right; }
  .topic--referral .topic__title { color: var(--red); text-align: left; }
  .topic--origin { left: 720px; top: 233px; width: 128px; }
  .topic--origin .topic__title { color: var(--green); }
  .topic--value { left: 670px; top: 562px; width: 202px; }
  .topic--value .topic__title { color: var(--purple); }
  .topic--ideal { left: 163px; top: 592px; width: 135px; text-align: center; }
  .topic--ideal .topic__title { color: var(--teal); }
  .topic--concept { left: 611px; top: 656px; width: 165px; }
  .topic--concept .topic__title { color: var(--green); }
  .brand {
    position: absolute; left: 900px; top: 298px; width: 255px;
    display: flex; flex-direction: column; align-items: center; gap: 10px;
  }
  .brand__mark { width: 140px; height: 140px; background: var(--navy); }
  .brand__name {
    font-family: "Noto Serif", Georgia, serif;
    font-weight: 400;
    font-size: 20px;
    line-height: 26px;
    letter-spacing: 0.5px;
    color: var(--navy);
    white-space: nowrap;
  }
</style>
</head>
<body>
<main class="board">
  <svg class="board__art" width="1200" height="763" viewBox="0 0 1200 763" aria-hidden="true">
    <defs>
      <linearGradient id="arc-red" x1="0" y1="1" x2="1" y2="0">
        <stop offset="0" stop-color="#ee5a5e"/><stop offset="1" stop-color="#f7a823"/>
      </linearGradient>
      <linearGradient id="arc-green" x1="0" y1="0" x2="1" y2="1">
        <stop offset="0" stop-color="#8dc63f"/><stop offset="0.6" stop-color="#2fb3c6"/><stop offset="1" stop-color="#4a3a8c"/>
      </linearGradient>
      <linearGradient id="arc-teal" x1="0" y1="0" x2="1" y2="0">
        <stop offset="0" stop-color="#f7a823"/><stop offset="1" stop-color="#8dc63f"/>
      </linearGradient>
      <linearGradient id="arc-purple" x1="0" y1="0" x2="1" y2="0">
        <stop offset="0" stop-color="#8dc63f"/><stop offset="0.5" stop-color="#2fb3c6"/><stop offset="1" stop-color="#4a3a8c"/>
      </linearGradient>
      <linearGradient id="arc-yellow" x1="0" y1="0" x2="1" y2="0">
        <stop offset="0" stop-color="#f26a2a"/><stop offset="0.5" stop-color="#f7a823"/><stop offset="1" stop-color="#8dc63f"/>
      </linearGradient>
    </defs>

    <g class="clouds" fill="var(--cloud)">
      <g transform="translate(962 118)">
        <circle cx="-40" cy="8" r="26"/><circle cx="0" cy="-14" r="36"/><circle cx="40" cy="6" r="28"/><circle cx="4" cy="26" r="30"/>
      </g>
      <g transform="translate(455 740)">
        <circle cx="-90" cy="20" r="40"/><circle cx="-30" cy="-20" r="55"/><circle cx="40" cy="0" r="50"/><circle cx="100" cy="25" r="40"/>
      </g>
      <g transform="translate(900 735)">
        <circle cx="-70" cy="25" r="40"/><circle cx="0" cy="-15" r="60"/><circle cx="80" cy="15" r="50"/><circle cx="150" cy="35" r="40"/>
      </g>
      <g transform="translate(330 610)"><circle cx="0" cy="0" r="22"/><circle cx="25" cy="-8" r="22"/><circle cx="45" cy="6" r="18"/></g>
      <g transform="translate(790 625)"><circle cx="0" cy="0" r="16"/><circle cx="20" cy="-6" r="18"/></g>
    </g>

    <g class="connectors" fill="none" stroke-width="2.5" stroke-linecap="round" stroke-linejoin="round">
      <path class="connector connector--red" d="M268 220 V232 H345" stroke="#f7a823"/>
      <path class="connector connector--referral" d="M268 232 V352 H248" stroke="#ee5a5e"/>
      <path class="connector connector--origin" d="M602 285 H695 V242" stroke="#8dc63f"/>
      <path class="connector connector--value" d="M602 285 V330 H655" stroke="#8dc63f"/>
      <path class="connector connector--stem" d="M448 401 H462 V472 H478 V488" stroke="url(#arc-teal)"/>
      <path class="connector connector--ideal" d="M325 548 V690 H135" stroke="#f26a2a"/>
      <path class="connector connector--ideal-base" d="M335 706 H145" stroke="#f26a2a" stroke-width="2"/>
      <path class="connector connector--concept" d="M598 598 V742 H788" stroke="#f26a2a"/>
    </g>

    <g class="arcs" fill="none" stroke-linecap="round" stroke-width="3">
      <path class="arc arc--red-outer" d="M151 192 A135 125 0 1 1 402 119" stroke="url(#arc-red)"/>
      <path class="arc arc--red-inner" d="M189 204 A112 104 0 0 1 230 32" stroke="#ee5a5e" stroke-width="2.5"/>

      <path class="arc arc--green-outer" d="M612 33 A122 112 0 0 1 800 154" stroke="url(#arc-green)"/>
      <path class="arc arc--green-inner" d="M608 41 A115 110 0 0 0 616 215 Q602 232 602 255 V285" stroke="#8dc63f" stroke-width="2.5"/>

      <path class="arc arc--teal-outer" d="M350 325 A128 118 0 1 1 598 285 H602" stroke="url(#arc-teal)"/>
      <path class="arc arc--teal-inner" d="M342 285 A128 118 0 0 0 448 401" stroke="#f7a823"/>

      <path class="arc arc--purple-outer" d="M575 385 A118 108 0 0 1 786 475" stroke="url(#arc-purple)" stroke-width="2.5"/>
      <path class="arc arc--purple-inner" d="M564 474 A112 104 0 0 0 769 499" stroke="url(#arc-purple)"/>

      <path class="arc arc--orange-outer" d="M213 347 A110 102 0 0 0 213 523" stroke="#ee5a5e" stroke-width="2.5"/>
      <path class="arc arc--orange-mid" d="M234 350 A98 90 0 0 0 176 466" stroke="#f26a2a" stroke-width="2"/>
      <path class="arc arc--orange-inner" d="M363 435 A95 88 0 0 1 236 518" stroke="#f26a2a" stroke-width="2"/>

      <path class="arc arc--yellow-outer" d="M368 543 A118 110 0 0 1 572 543" stroke="url(#arc-yellow)" stroke-width="2.5"/>
      <path class="arc arc--yellow-inner" d="M359 645 A122 112 0 0 0 570 662" stroke="#f7a823"/>
    </g>

    <g class="dots">
      <circle cx="189" cy="204" r="4" fill="#ee5a5e"/>
      <circle cx="695" cy="240" r="4" fill="#8dc63f"/>
      <circle cx="350" cy="325" r="4" fill="#2fb3c6"/>
      <circle cx="575" cy="385" r="4" fill="#5a4597"/>
      <circle cx="363" cy="435" r="4" fill="#ee5a5e"/>
      <circle cx="368" cy="543" r="4" fill="#f7a823"/>
    </g>

    <g class="hubs">
      <g class="hub hub--red">
        <ellipse cx="268" cy="130" rx="100" ry="90" fill="var(--red-halo)"/>
        <ellipse cx="268" cy="131" rx="92" ry="83" fill="var(--red-deep)"/>
        <ellipse cx="268" cy="128" rx="83" ry="75" fill="var(--red-soft)"/>
      </g>
      <g class="hub hub--green">
        <ellipse cx="682" cy="125" rx="87" ry="80" fill="var(--green-halo)"/>
        <ellipse cx="682" cy="126" rx="80" ry="73" fill="var(--green-deep)"/>
        <ellipse cx="682" cy="123" rx="72" ry="66" fill="var(--green-soft)"/>
      </g>
      <g class="hub hub--teal">
        <ellipse cx="470" cy="285" rx="100" ry="90" fill="var(--teal-halo)"/>
        <ellipse cx="470" cy="286" rx="92" ry="83" fill="var(--teal-deep)"/>
        <ellipse cx="470" cy="283" rx="83" ry="75" fill="var(--teal-soft)"/>
      </g>
      <g class="hub hub--orange">
        <ellipse cx="268" cy="435" rx="80" ry="73" fill="var(--orange)"/>
        <ellipse cx="268" cy="432" rx="69" ry="62" fill="var(--orange-soft)"/>
      </g>
      <g class="hub hub--purple">
        <ellipse cx="672" cy="447" rx="100" ry="92" fill="var(--purple-halo)"/>
        <ellipse cx="672" cy="448" rx="92" ry="84" fill="var(--purple-deep)"/>
        <ellipse cx="672" cy="445" rx="83" ry="76" fill="var(--purple-soft)"/>
      </g>
      <g class="hub hub--yellow">
        <ellipse cx="470" cy="598" rx="100" ry="90" fill="var(--yellow-halo)"/>
        <ellipse cx="470" cy="599" rx="92" ry="83" fill="var(--yellow)"/>
        <ellipse cx="470" cy="596" rx="83" ry="75" fill="var(--yellow-soft)"/>
      </g>
    </g>
  </svg>

  <section class="topic topic--growth">
    <h2 class="topic__title">Why Growth Is<br>Necessary?</h2>
    <p class="topic__body">Lorem ipsum dolor sit amet, consectetuer adipiscing elit. Aenean commodo ligula eget dolor. Aenean massa.</p>
  </section>

  <section class="topic topic--referral">
    <h2 class="topic__title">Referral Culture Stories</h2>
    <p class="topic__body">Lorem ipsum dolor sit amet, consectetuer adipiscing elit. Aenean commodo ligula eget dolor. Aenean massa.</p>
  </section>

  <section class="topic topic--origin">
    <h2 class="topic__title">Origin Story</h2>
    <p class="topic__body">Lorem ipsum dolor sit amet, consectetuer adipiscing elit. Aenean commodo ligula eget dolor. Aenean massa.</p>
  </section>

  <section class="topic topic--value">
    <h2 class="topic__title">Client Value Proposition</h2>
    <p class="topic__body">Lorem ipsum dolor sit amet, consectetuer adipiscing elit. Aenean commodo ligula eget dolor. Aenean massa.</p>
  </section>

  <section class="topic topic--ideal">
    <h2 class="topic__title">Ideal Client</h2>
    <p class="topic__body">Lorem ipsum dolor sit amet, consectetuer adipiscing elit. Aenean commodo ligula eget dolor. Aenean massa.</p>
  </section>

  <section class="topic topic--concept">
    <h2 class="topic__title">Singular Concept</h2>
    <p class="topic__body">Lorem ipsum dolor sit amet, consectetuer adipiscing elit. Aenean commodo ligula eget dolor. Aenean massa.</p>
  </section>

  <div class="brand">
    <span class="brand__mark"></span>
    <p class="brand__name">Harlow Financial Advisors</p>
  </div>
</main>
</body>
</html>
```